Website design for luxury private hair salon

I'm looking for someone to use my Logo and build me a website for my webpage www.lunetresses.com.au (You can have a look at it as it has every detail I need included on it already), however I want a fresh new appearance and it to look and feel super stylish.

I am thinking colours in black, with silver or white, beautiful hair images like the ones you'll see on the current webpage - the price list as per what you already see.

I will include a copy of my biz card on here, so you can see the feel of the card, and design a website with a similar feel. It is matt black with a foil silver.

Modern, but classic and fresh. I will also need you to be able to publish it to my URL for me as I have no idea how to do this. I need it up and running pronto!

The website will need to be able to be read clearly on all devices incluing smart phones and ipads. The URL is currently registered and hosted by Nimbo Vault

Thinking a Home Page - large logo etc and write up on who and what we offer
Services/Price List page - as per the price list on my current webpage
Contact Page - with a built in contact form.

Target Market(s)

Middle aged, fashionable, stylish women and men who enjoy luxury hair care and styling in an upmarket location.

Industry/Entity Type

Hair And Beauty

Number of Pages Required

3 page

Font styles to use
Other font styles liked:
• see my images for my current logo

Colors
000000
b2b2b2
a54499

Requirements
Must have
• Style
• Fast turnaround
• Be viewable on all devices, PC, ipads, smart phones
• Designer able to upload it so its a running website for me to my URL
Nice to have
• Just a really feminine, stylish website which is easy to read and shows some beautiful images of perfect hair
Should not have
• Browns, reds or orange colours.

```html
<!DOCTYPE html>
<html lang="en">
<head>
<meta charset="utf-8">
<title>Lune hair &amp; body</title>
<link rel="stylesheet" href="https://fonts.googleapis.com/css2?family=Raleway:wght@300;400;500;600&family=Great+Vibes&display=swap">
<style>
:root{
  --black:#000000;
  --ink:#0b0a0c;
  --band:#141216;
  --silver:#b2b2b2;
  --white:#ffffff;
  --plum:#a54499;
  --plum-soft:#c15bb4;
  --plum-deep:#7e2f75;
  --paper:#f1f0f1;
  --sans:'Raleway',Arial,sans-serif;
  --script:'Great Vibes',cursive;
}
*{box-sizing:border-box;margin:0;padding:0}
html,body{width:1200px;height:2206px;overflow:hidden;background:var(--black)}
body{position:relative;font-family:var(--sans);color:var(--white)}
.abs{position:absolute}
a{color:inherit;text-decoration:none}

/* top bar */
.topbar{left:0;top:0;width:1200px;height:44px;background:var(--black);z-index:3}
.topbar .phones{left:170px;top:14px;font-size:11px;letter-spacing:.3px;color:#ddd;display:flex;align-items:center;gap:8px}
.social{display:flex;gap:20px}
.social span{width:16px;height:16px;border:1.4px solid #aaa;border-radius:50%;display:block}
.topbar .social{left:900px;top:14px}

/* nav */
.nav{left:0;top:44px;width:1200px;height:68px;background:rgba(0,0,0,.55);z-index:3}
.brand{left:170px;top:14px;font-size:34px;font-weight:400;color:var(--white);letter-spacing:1px;line-height:1}
.brand small{display:block;font-size:9px;letter-spacing:1.5px;text-align:right;margin-top:2px}
.menu{left:616px;top:27px;font-size:11px;color:#ddd;display:flex;gap:14px}
.menu .on{color:var(--plum-soft)}
.menu i{font-style:normal;color:#888}
.btn-book{left:869px;top:21px;width:158px;height:28px;border-radius:14px;background:var(--plum);font-size:10px;font-weight:600;display:flex;align-items:center;justify-content:center;letter-spacing:.2px}

/* hero */
.hero{left:0;top:0;width:1200px;height:545px;background:radial-gradient(ellipse at 30% 45%,#6a6a6a 0%,#2e2e2e 40%,#111 75%),#111}
.hero-name{left:680px;top:160px;width:360px;text-align:center;font-size:104px;font-weight:400;line-height:1;letter-spacing:2px}
.hero-sub{left:680px;top:300px;width:360px;text-align:center;font-size:28px;font-weight:400;letter-spacing:3px;padding-left:40px}
.hero-tag{left:700px;top:350px;width:360px;text-align:center;font-family:var(--script);font-size:46px;line-height:64px}

/* about */
.about{left:0;top:545px;width:1200px;height:376px;background:linear-gradient(90deg,#141014 0%,#221a22 45%,#2a2028 70%,#0f0c10 100%)}
.about-photo{left:720px;top:0;width:480px;height:376px;background:radial-gradient(ellipse at 55% 45%,#5a5055 0%,#2a2228 55%,transparent 80%)}
h2.title{font-weight:400;font-size:36px;line-height:1}
h2.title em{font-family:var(--script);font-style:normal;color:var(--plum-soft);font-size:44px}
.about h2{left:191px;top:52px}
.about p{left:191px;top:108px;width:435px;font-size:13px;line-height:18px;color:#e6e6e6}
.about .lead{left:191px;top:222px;font-size:34px;font-weight:400}
.about .script{left:191px;top:260px;font-family:var(--script);font-size:62px;color:var(--plum-soft);line-height:1.1}

/* brand band */
.brands{left:0;top:921px;width:1200px;height:173px;background:var(--paper)}
.brands .mark{left:238px;top:14px;font-size:34px;font-weight:500;color:var(--plum);letter-spacing:3px}
.brands .mark small{display:block;font-size:6px;letter-spacing:1px;margin-top:-2px;color:var(--plum-deep)}
.shelf{left:257px;top:58px;width:684px;height:110px;background:linear-gradient(90deg,#e9e4ea 0%,#c9a7cf 35%,#e3c9a2 55%,#6ec4cc 72%,#2a2a2a 90%,#e9e4ea 100%);opacity:.85}

/* services */
.services{left:0;top:1094px;width:1200px;height:388px;background:radial-gradient(ellipse at 50% 55%,#2a2428 0%,#121012 65%)}
.services h2{left:0;width:1200px;top:54px;text-align:center}
.svc{width:170px;text-align:center;font-size:18px;color:var(--white)}
.svc svg{display:block;margin:0 auto 12px;width:40px;height:40px;stroke:var(--plum-soft);fill:none;stroke-width:1.8;stroke-linecap:round;stroke-linejoin:round}

/* call to action */
.cta{left:0;top:1482px;width:1200px;height:188px;background:linear-gradient(90deg,var(--plum) 0%,var(--plum) 55%,#b65aab 75%,var(--plum-deep) 100%)}
.cta p{left:191px;top:58px;font-size:29px;line-height:37px;font-weight:400}
.btn-line{border:2px solid var(--white);border-radius:20px;display:flex;align-items:center;justify-content:center;font-weight:600}
.cta .btn-line{left:747px;top:74px;width:260px;height:38px;font-size:17px}

/* contact */
.contact{left:0;top:1670px;width:1200px;height:401px;background:linear-gradient(180deg,#1a1a1c 0%,#0e0e10 100%)}
.contact h2{left:0;width:1200px;top:50px;text-align:center}
.field{border-bottom:1px solid #9a9a9a;border-left:1px solid #9a9a9a;height:22px;font-size:13px;font-style:italic;color:#ccc;padding-left:6px;line-height:16px}
.f-name{left:415px;top:130px;width:176px}
.f-mail{left:609px;top:130px;width:178px}
.f-msg{left:415px;top:213px;width:372px}
.contact .btn-line{left:562px;top:266px;width:76px;height:30px;font-size:11px;border-width:1.5px}
.contact .phones{left:0;width:1200px;top:337px;text-align:center;font-size:18px;letter-spacing:.5px;color:#e6e6e6}

/* footer */
.footer{left:0;top:2071px;width:1200px;height:135px;background:var(--black)}
.footer .social{left:532px;top:32px;gap:24px}
.footer .social span{width:18px;height:18px}
.footer nav{left:0;width:1200px;top:66px;text-align:center;font-size:10px;color:#ddd}
.footer nav .on{color:var(--plum-soft)}
.footer nav i{font-style:normal;margin:0 10px;color:#888}
.footer .copy{left:0;width:1200px;top:93px;text-align:center;font-size:10px;color:#ddd}
.footer .copy b{font-weight:400;color:var(--plum-soft)}
</style>
</head>
<body>

<section class="abs hero" role="img" aria-label="Black and white portrait of a woman in a fur-trimmed hood"></section>

<header class="abs topbar">
  <div class="abs phones">
    <svg width="12" height="12" viewBox="0 0 24 24" fill="none" stroke="#ccc" stroke-width="2"><path d="M5 3h4l2 5-2.5 1.5a11 11 0 0 0 6 6L16 13l5 2v4a2 2 0 0 1-2 2A17 17 0 0 1 3 5a2 2 0 0 1 2-2z"/></svg>
    <span>ADA 0400 123 456 , NINA 0400 987 654</span>
  </div>
  <div class="abs social"><span></span><span></span><span></span><span></span></div>
</header>

<nav class="abs nav">
  <div class="abs brand">Lune<small>hair &amp; body</small></div>
  <div class="abs menu"><a class="on">Home</a><i>|</i><a>Services &amp; Price List</a><i>|</i><a>Contact us</a></div>
  <a class="abs btn-book">BOOK AN APPOINTMENT</a>
</nav>

<div class="abs hero-name">Lune</div>
<div class="abs hero-sub">hair &amp; body</div>
<div class="abs hero-tag">Loves the Hair<br>You Hate.</div>

<section class="abs about">
  <div class="abs about-photo" role="img" aria-label="Portrait of a woman with dark flowing hair and bold makeup"></div>
  <h2 class="abs title">About <em>us</em></h2>
  <p class="abs">"We pride ourselves on being able to offer a private salon experience to our clients in the exclusive suburb of Elmsford, where your hair design and colouring needs will be met with years of experience and current industry training and knowledge".</p>
  <div class="abs lead">We Give You the</div>
  <div class="abs script">Best Hair Colour</div>
</section>

<section class="abs brands">
  <div class="abs mark">AURELLE<small>CARE FOR EVERY STRAND</small></div>
  <div class="abs shelf" role="img" aria-label="Row of hair care product bottles"></div>
</section>

<section class="abs services">
  <h2 class="abs title">Our <em>services</em></h2>
  <div class="abs svc" style="left:144px;top:140px">
    <svg viewBox="0 0 40 40"><path d="M8 32 30 10M26 8l6 6M14 26l-4 4"/></svg>Hair Cuts</div>
  <div class="abs svc" style="left:325px;top:140px">
    <svg viewBox="0 0 40 40"><path d="M8 32l12-12M18 14l8 8M22 10l8 8 4-4-8-8z"/></svg>Colouring</div>
  <div class="abs svc" style="left:505px;top:140px">
    <svg viewBox="0 0 40 40"><path d="M10 30l4-10 14-14 6 6-14 14zM14 20l6 6M8 34h10"/></svg>Highlighting</div>
  <div class="abs svc" style="left:684px;top:140px">
    <svg viewBox="0 0 40 40"><rect x="13" y="16" width="14" height="16" rx="2"/><path d="M17 16v-4h6v4M20 12V8"/></svg>Extensions</div>
  <div class="abs svc" style="left:865px;top:140px">
    <svg viewBox="0 0 40 40"><path d="M14 4l4 20M22 4l-2 20M18 24l-2 10h8l-2-10"/></svg>Straightening</div>
  <div class="abs svc" style="left:387px;top:268px">
    <svg viewBox="0 0 40 40"><circle cx="20" cy="16" r="8"/><path d="M8 36c0-8 5-12 12-12s12 4 12 12M12 16c0-9 16-9 16 0"/></svg>Bridal Treatments</div>
  <div class="abs svc" style="left:622px;top:268px">
    <svg viewBox="0 0 40 40"><rect x="8" y="12" width="10" height="22" rx="2"/><rect x="22" y="8" width="10" height="26" rx="2"/></svg>Products &amp; Advice</div>
</section>

<section class="abs cta" role="img" aria-label="Faint profile of a woman over a plum tint">
  <p class="abs">Wana do something with with your<br>Hairs? So Meet us</p>
  <a class="abs btn-line">BOOK AN APPOINTMENT</a>
</section>

<section class="abs contact" role="img" aria-label="Dim close-up of hands typing on a keyboard">
  <h2 class="abs title">Contact <em>us</em></h2>
  <div class="abs field f-name">Name</div>
  <div class="abs field f-mail">E-mail</div>
  <div class="abs field f-msg">Message</div>
  <a class="abs btn-line">Send</a>
  <div class="abs phones">ADA &nbsp;0400 123 456 &nbsp;| &nbsp;NINA &nbsp;0400 987 654</div>
</section>

<footer class="abs footer">
  <div class="abs social"><span></span><span></span><span></span><span></span></div>
  <nav class="abs"><a class="on">Home</a><i>|</i><a>Services &amp; Price List</a><i>|</i><a>Contact us</a></nav>
  <div class="abs copy">©2017 All rights reserved. <b>Lune hair &amp; body</b></div>
</footer>

</body>
</html>
```